R&t subterra

We specialize in CIPP pipe lining but do other underground utilities trenchless as well.

Target Market(s)

Trenchless sewer replacement

Contact Information for Business Card

Doug Falvey 715-482-6170 Pine Hollow, WI

```html
<!DOCTYPE html>
<html lang="en">
<head>
<meta charset="utf-8">
<title>R&amp;t subterra – Business Cards</title>
<link rel="stylesheet" href="https://fonts.googleapis.com/css2?family=Roboto:wght@400&family=Ubuntu:wght@500;700&display=swap">
<style>
  :root {
    --backdrop: #2a2a2a;
    --card: #1f2021;
    --card-edge: #2b2c2e;
    --blue: #1a78c2;
    --blue-light: #2fa6da;
    --grey: #8a8a8a;
    --text-light: #e6e6e6;
    --text-muted: #9a9a9a;
    --faint: #263440;
  }
  * { box-sizing: border-box; margin: 0; padding: 0; }
  html, body { width: 1200px; height: 1138px; overflow: hidden; background: var(--backdrop); }
  .canvas { position: relative; width: 1200px; height: 1138px; }

  .card {
    position: absolute;
    border-radius: 16px;
    overflow: hidden;
    background: linear-gradient(160deg, #1b1c1d 0%, var(--card) 55%, var(--card-edge) 100%);
  }

  /* Front */
  .card-front { left: 274px; top: 186px; width: 623px; height: 376px; }
  .front-brand {
    position: absolute; left: 0; right: 0; top: 152px;
    display: flex; align-items: center; justify-content: center; gap: 16px;
  }
  .brand-dot { width: 54px; height: 54px; border-radius: 50%; background: var(--blue); flex: none; }
  .brand-name {
    font-family: "Ubuntu", sans-serif; font-weight: 700;
    color: var(--blue); line-height: 1; white-space: nowrap;
  }
  .front-brand .brand-name { font-size: 56px; }
  .front-web {
    position: absolute; left: 0; right: 0; top: 326px;
    display: flex; align-items: center; justify-content: center; gap: 16px;
  }
  .web-rule { width: 90px; height: 2px; background: linear-gradient(90deg, var(--blue) 0 30%, var(--blue-light) 30% 60%, var(--grey) 60% 100%); }
  .web-rule.right { background: linear-gradient(90deg, var(--blue) 0 35%, var(--blue-light) 35% 60%, var(--grey) 60% 100%); }
  .web-text { font-family: "Roboto", sans-serif; font-size: 16px; color: var(--text-muted); }

  /* Back */
  .card-back { left: 276px; top: 608px; width: 618px; height: 374px; }
  .side-band { position: absolute; left: 0; top: 0; width: 47px; height: 100%;
    background: linear-gradient(var(--blue) 0 188px, var(--blue-light) 188px 100%); }
  .side-stripe { position: absolute; left: 57px; top: 0; width: 9px; height: 100%; background: var(--grey); }
  .faint-mark { position: absolute; left: 322px; top: 92px; width: 272px; height: 272px; }
  .back-brand { position: absolute; left: 88px; top: 42px; display: flex; align-items: center; gap: 12px; }
  .back-brand .brand-dot { width: 42px; height: 42px; }
  .back-brand .brand-name { font-size: 40px; }
  .person { position: absolute; left: 98px; top: 172px; }
  .person-name { font-family: "Ubuntu", sans-serif; font-weight: 500; font-size: 26px; color: var(--blue); line-height: 1.1; }
  .person-title { font-family: "Roboto", sans-serif; font-size: 16px; color: var(--text-light); margin-top: 4px; }
  .contacts { position: absolute; left: 98px; top: 258px; list-style: none; }
  .contacts li { display: flex; align-items: center; gap: 12px; height: 22.5px;
    font-family: "Roboto", sans-serif; font-size: 16px; color: var(--text-light); }
  .contacts svg { width: 14px; height: 14px; fill: var(--blue); flex: none; }
</style>
</head>
<body>
<div class="canvas">

  <section class="card card-front">
    <div class="front-brand">
      <span class="brand-dot"></span>
      <span class="brand-name">R&amp;t subterra</span>
    </div>
    <div class="front-web">
      <span class="web-rule"></span>
      <span class="web-text">www.rtsubterra.com</span>
      <span class="web-rule right"></span>
    </div>
  </section>

  <section class="card card-back">
    <div class="side-band"></div>
    <div class="side-stripe"></div>
    <svg class="faint-mark" viewBox="0 0 272 272" aria-hidden="true"><circle cx="136" cy="136" r="136" fill="var(--faint)" opacity="0.7"/></svg>

    <div class="back-brand">
      <span class="brand-dot"></span>
      <span class="brand-name">R&amp;t subterra</span>
    </div>

    <div class="person">
      <div class="person-name">Doug Falvey</div>
      <div class="person-title">Managing Director</div>
    </div>

    <ul class="contacts">
      <li><svg viewBox="0 0 16 16"><path d="M2 6c0-2 3-3 6-3s6 1 6 3v1h-3V5.5H5V7H2zM4 8h8l2 5H2z"/></svg>715-482-6170</li>
      <li><svg viewBox="0 0 16 16"><path d="M1 3h14v10H1zM2.5 4.5 8 9l5.5-4.5v-.2H2.5z" fill-rule="evenodd"/></svg>doug@rtsubterra.com</li>
      <li><svg viewBox="0 0 16 16"><path d="M8 1a7 7 0 1 0 0 14A7 7 0 0 0 8 1zm0 1.5c.8 0 1.7 1.9 1.9 4.5H6.1C6.3 4.4 7.2 2.5 8 2.5zM2.6 8.5h2.5c.1 1.8.5 3.3 1.1 4.3a5.5 5.5 0 0 1-3.6-4.3zm0-1.5A5.5 5.5 0 0 1 6.2 3.2C5.6 4.2 5.2 5.6 5.1 7zm3.5 1.5h3.8c-.2 2.6-1.100 4.5-1.900 4.5s-1.7-1.9-1.9-4.5zm4.8 0h2.5a5.5 5.5 0 0 1-3.6 4.3c.6-1 1-2.5 1.1-4.3zm0-1.5c-.1-1.4-.5-2.8-1.1-3.8A5.5 5.5 0 0 1 13.4 7z"/></svg>www.rtsubterra.com</li>
      <li><svg viewBox="0 0 16 16"><path d="M8 1a5 5 0 0 0-5 5c0 3.5 5 9 5 9s5-5.5 5-9a5 5 0 0 0-5-5zm0 7a2 2 0 1 1 0-4 2 2 0 0 1 0 4z"/></svg>Pine Hollow, WI</li>
    </ul>
  </section>

</div>
</body>
</html>
```